Business Cards for Project Management Consulting Company
Brightfold Consulting
Business Cards for Project Management Consulting Company - Consulting
Creative Brief
Simple
Miriam Quenby, PMP
Director, Project Manager
512 Pellow Street Victoria, BC V9R 2K4
mquenby@brightfoldconsulting.example
www.brightfoldconsulting.example

```html
<!DOCTYPE html>
<html lang="en">
<head>
<meta charset="utf-8">
<title>Brightfold Consulting – Business Cards</title>
<link href="https://fonts.googleapis.com/css2?family=Arimo:wght@400&display=swap" rel="stylesheet">
<style>
  :root {
    --backdrop: #6a6a6a;
    --card: #ffffff;
    --green: #94c11f;
    --grey: #6d6e70;
    --grey-light: #9a9b9d;
  }
  html, body {
    margin: 0;
    padding: 0;
    width: 1200px;
    height: 440px;
    overflow: hidden;
    background: var(--backdrop);
    font-family: "Arimo", Arial, sans-serif;
  }
  .canvas {
    position: relative;
    width: 1200px;
    height: 440px;
  }
  .card {
    position: absolute;
    top: 70px;
    height: 281px;
    background: var(--card);
  }
  .card--front { left: 29px; width: 517px; }
  .card--back { left: 568px; width: 612px; }

  /* Front */
  .brand-square {
    position: absolute;
    left: 92px;
    top: 150px;
    width: 100px;
    height: 100px;
    background: var(--green);
  }
  .card--front .brand-square { top: 90px; }
  .divider {
    position: absolute;
    left: 220px;
    top: 92px;
    width: 2px;
    height: 96px;
    background: var(--grey-light);
  }
  .wordmark {
    position: absolute;
    left: 238px;
    top: 96px;
    color: var(--green);
    font-weight: 400;
    line-height: 1;
  }
  .wordmark__main { display: block; font-size: 46px; letter-spacing: -0.5px; }
  .wordmark__sub { display: block; font-size: 30px; letter-spacing: 4.5px; margin-top: 8px; }

  /* Back */
  .card--back .brand-block {
    position: absolute;
    left: 27px;
    top: 59px;
    width: 180px;
    height: 180px;
  }
  .card--back .brand-square {
    left: 0;
    top: 0;
    width: 82px;
    height: 82px;
  }
  .card--back .wordmark {
    left: 0;
    top: 100px;
  }
  .card--back .wordmark__main { font-size: 30px; }
  .card--back .wordmark__sub { font-size: 20px; letter-spacing: 3px; margin-top: 6px; }

  .person {
    position: absolute;
    left: 229px;
    top: 36px;
  }
  .person__name {
    margin: 0;
    color: var(--green);
    font-size: 19px;
    font-weight: 400;
  }
  .person__title {
    margin: 6px 0 0;
    color: var(--grey);
    font-size: 15px;
  }
  .contacts {
    position: absolute;
    left: 232px;
    top: 108px;
    margin: 0;
    padding: 0;
    list-style: none;
    color: var(--grey);
    font-size: 13px;
    line-height: 18px;
  }
  .contacts li {
    display: flex;
    align-items: flex-start;
    margin-bottom: 6px;
  }
  .contacts svg {
    flex: none;
    width: 14px;
    height: 14px;
    margin: 2px 10px 0 0;
    fill: var(--green);
  }
  .contacts .address { margin-bottom: 8px; }
</style>
</head>
<body>
<main class="canvas">
  <section class="card card--front" aria-label="Card front">
    <div class="brand-square" aria-hidden="true"></div>
    <div class="divider" aria-hidden="true"></div>
    <div class="wordmark">
      <span class="wordmark__main">Brightfold</span>
      <span class="wordmark__sub">consulting</span>
    </div>
  </section>

  <section class="card card--back" aria-label="Card back">
    <div class="brand-block">
      <div class="brand-square" aria-hidden="true"></div>
      <div class="wordmark">
        <span class="wordmark__main">Brightfold</span>
        <span class="wordmark__sub">consulting</span>
      </div>
    </div>

    <div class="person">
      <h1 class="person__name">Miriam Quenby, PMP</h1>
      <p class="person__title">Director, Project Manager</p>
    </div>

    <ul class="contacts">
      <li class="address">
        <svg viewBox="0 0 16 16" aria-hidden="true"><path d="M8 1 1 7.5h2V15h4v-4h2v4h4V7.5h2z"/></svg>
        <span>512 Pellow Street<br>Victoria, BC<br>V9R 2K4</span>
      </li>
      <li>
        <svg viewBox="0 0 16 16" aria-hidden="true"><path d="M4 1h8a1 1 0 0 1 1 1v12a1 1 0 0 1-1 1H4a1 1 0 0 1-1-1V2a1 1 0 0 1 1-1zm1 2v8h6V3zm3 9.2a1 1 0 1 0 0 2 1 1 0 0 0 0-2z"/></svg>
        <span>250-555-0147</span>
      </li>
      <li>
        <svg viewBox="0 0 16 16" aria-hidden="true"><path d="M1 3h14v10H1zm1.5 1.5v.4L8 9l5.5-4.1v-.4zm0 2.2v4.8h11V6.7L8 10.8z"/></svg>
        <span>mquenby@brightfoldconsulting.example</span>
      </li>
      <li>
        <svg viewBox="0 0 16 16" aria-hidden="true"><path d="M8 1a7 7 0 1 0 0 14A7 7 0 0 0 8 1zm0 1.5c.8 0 1.7 1.6 2 4H6c.3-2.4 1.2-4 2-4zM5.7 3A8.5 8.5 0 0 0 4.6 6.5H2.8A5.6 5.6 0 0 1 5.7 3zm4.6 0a5.6 5.6 0 0 1 2.9 3.5h-1.8A8.5 8.5 0 0 0 10.3 3zM2.6 8h2A9 9 0 0 0 4.7 9.5H2.8A5.5 5.5 0 0 1 2.6 8zm3.5 0h3.8a8 8 0 0 1-.1 1.5H6.2A8 8 0 0 1 6.1 8zm5.3 0h2a5.5 5.5 0 0 1-.2 1.5h-1.9a9 9 0 0 0 .1-1.5zM3.4 11h1.6c.2.8.5 1.5.9 2a5.6 5.6 0 0 1-2.5-2zm3.1 0h3c-.4 1.6-1 2.5-1.5 2.5S6.9 12.6 6.5 11zm4.5 0h1.6a5.6 5.6 0 0 1-2.5 2c.4-.5.7-1.2.9-2z"/></svg>
        <span>www.brightfoldconsulting.example</span>
      </li>
    </ul>
  </section>
</main>
</body>
</html>
```